Book Cover Design for first time business owners

Looking for a design for my book, 'FORGING A VENTURE' subtitle is
THE LEASING, LAYOUT, & BUILD-OUT METHODS FOR LAUNCHING YOUR SHOP OR EATERY IDEA WITHOUT DELAYS OR OVERSPENDING

If it helps, below is part of the preface:

These pages derive from my experiences and industry standards. This book runs through the budgeting, real estate, design, construction, signage, and equipment processes needed to get any retail or restaurant space open on-time and on budget while saving you time, money, and headaches along the way.

Whether it be a one-off enterprise or franchise, flower shop, or swim center; the steps and procedures are strikingly similar. Whether you’re looking to spend $200,000 or $2,000,000, it’s all largely the same.
This book does not discuss marketing or operations as those items are more concept specific, and outside the confines of this book.
Technically food-service concepts (restaurants, cafés, and bars) are not considered retail. For the basis of this book and to streamline writing, mentions of retail include food-service concepts.

Target Market(s)

First time business Owners looking to construct a retail or food-service concept

Font styles to use
Serif

Requirements
Must have
• I'm open to any designs! Looking for the design to wrap around the front, spine, and back.
• Please include the authors name on the front: Corwin Delaugh. The Authors name size should not be overly intrusive.
• I'm still working on the verbiage for the back of the book. That verbiage will be on the top half of the back.

```html
<!DOCTYPE html>
<html lang="en">
<head>
<meta charset="utf-8">
<title>Forging a Venture — Book Cover</title>
<link href="https://fonts.googleapis.com/css2?family=Teko:wght@500&family=Libre+Caslon+Text:wght@400&display=swap" rel="stylesheet">
<style>
  :root {
    --cover-black: #1a1a1a;
    --cover-black-deep: #111111;
    --ink-white: #f4f4f4;
    --accent-red: #d8262d;
    --figure-light: #4a4a4a;
    --figure-dark: #2a2a2a;
  }
  html, body {
    margin: 0;
    padding: 0;
    overflow: hidden;
    background: var(--cover-black-deep);
  }
  .cover {
    position: relative;
    width: 993px;
    height: 1200px;
    overflow: hidden;
    background:
      radial-gradient(ellipse at 50% 40%, #222222 0%, var(--cover-black) 55%, var(--cover-black-deep) 100%);
  }
  .cover__subtitle {
    position: absolute;
    top: 48px;
    left: 60px;
    right: 60px;
    margin: 0;
    font-family: "Teko", "Arial Narrow", sans-serif;
    font-weight: 500;
    font-size: 33px;
    line-height: 36px;
    letter-spacing: 0.5px;
    text-align: center;
    color: var(--ink-white);
    text-transform: uppercase;
  }
  .cover__emblem {
    position: absolute;
    top: 185px;
    left: 300px;
    width: 360px;
    height: 610px;
  }
  .cover__title {
    position: absolute;
    top: 800px;
    left: 0;
    right: 0;
    margin: 0;
    font-family: "Libre Caslon Text", "Times New Roman", serif;
    font-weight: 400;
    font-size: 84px;
    line-height: 96px;
    text-transform: uppercase;
  }
  .cover__title-line {
    display: block;
  }
  .cover__title-line--lead {
    color: var(--accent-red);
    padding-left: 120px;
  }
  .cover__title-line--main {
    color: var(--ink-white);
    padding-left: 205px;
  }
  .cover__author {
    position: absolute;
    top: 1085px;
    left: 0;
    right: 0;
    margin: 0;
    text-align: center;
    font-family: "Libre Caslon Text", "Times New Roman", serif;
    font-size: 26px;
    letter-spacing: 1px;
    text-transform: uppercase;
    color: var(--accent-red);
  }
</style>
</head>
<body>
  <main class="cover">
    <p class="cover__subtitle">The Leasing, Layout, &amp; Build-Out Methods for Launching Your Shop or Eatery Idea Without Delays or Overspending</p>

    <svg class="cover__emblem" viewBox="0 0 360 610" role="img" aria-label="Large white dollar sign illustration with silhouetted profiles formed inside its curves">
      <defs>
        <linearGradient id="emblem-fill" x1="0" y1="0" x2="0" y2="1">
          <stop offset="0" stop-color="var(--figure-light)"/>
          <stop offset="1" stop-color="var(--figure-dark)"/>
        </linearGradient>
      </defs>
      <rect x="0" y="0" width="360" height="610" rx="6" fill="url(#emblem-fill)"/>
    </svg>

    <h1 class="cover__title">
      <span class="cover__title-line cover__title-line--lead">Forging a</span>
      <span class="cover__title-line cover__title-line--main">Venture</span>
    </h1>

    <p class="cover__author">Corwin Delaugh</p>
  </main>
</body>
</html>
```